Bamboo & Ember Business Card FUN & EXCITING

Here is the Information for the Card:
Harpreet Kalra (Toby)
E: TobyKalra@mailbox-demo.com
C: (480) 555-0147
www.BambooEmberLV.com

We don't want traditional Indian cliche, We a playful bold and fun business card.

Files: https://files.sharebox-demo.net/folders/7QtpLmzR2xVbN4kHs9wYcDfJ3eGaUoPi

https://files.sharebox-demo.net/folders/5ZrqTwyX8mKcE2vBn6aLpHsQ9uFjRgOe

Target Market(s)

Las Vegas Local Restaurant

Industry/Entity Type

Indian Restaurant

Contact Information for Business Card

Name, Email, Cell Phone, Company Logo

```html
<!DOCTYPE html>
<html lang="en">
<head>
<meta charset="utf-8">
<title>Bamboo &amp; Ember — Business Card</title>
<link rel="stylesheet" href="https://fonts.googleapis.com/css2?family=Anton&family=Roboto+Condensed:wght@700&family=Montserrat:wght@400&family=Bree+Serif&family=Oswald:wght@400&display=swap">
<style>
  :root {
    --backdrop: #2b2b2b;
    --cream: #fcf5dc;
    --paper: #ffffff;
    --ink: #111111;
    --muted: #6b6b6b;
    --pink: #e36b93;
    --orange: #ee7b2a;
    --art-light: #f6ecd0;
    --art-warm: #f1b27a;
  }
  * { box-sizing: border-box; margin: 0; padding: 0; }
  html, body {
    width: 1200px; height: 1108px; overflow: hidden;
    background: var(--backdrop);
  }
  .stage {
    position: relative; width: 1200px; height: 1108px;
    display: flex; justify-content: center; align-items: center; gap: 60px;
  }
  .card {
    position: relative; width: 430px; height: 720px;
    border-radius: 26px; overflow: hidden;
  }
  /* front */
  .card--front { background: var(--cream); }
  .brand-name {
    position: absolute; left: 40px; right: 40px; top: 110px;
    font-family: "Anton", sans-serif; font-size: 92px; line-height: 0.95;
    color: var(--ink); text-align: center; text-transform: uppercase;
  }
  .brand-location {
    position: absolute; right: 58px; top: 318px;
    font-family: "Bree Serif", serif; font-size: 22px; color: var(--ink);
  }
  .front-art {
    position: absolute; left: 70px; top: 360px; width: 290px; height: 210px;
    border-radius: 40px;
    background: radial-gradient(ellipse at 50% 45%, var(--art-light) 0%, var(--art-warm) 75%, var(--cream) 100%);
  }
  .tagline {
    position: absolute; left: 0; right: 0; top: 588px; text-align: center;
    font-family: "Oswald", sans-serif; font-size: 19px; color: var(--ink);
    letter-spacing: 0.5px;
  }
  /* back */
  .card--back { background: var(--paper); }
  .holder-name {
    position: absolute; left: 0; right: 0; top: 70px; text-align: center;
    font-family: "Roboto Condensed", sans-serif; font-weight: 700;
    font-size: 34px; color: var(--ink);
  }
  .icon-row {
    position: absolute; left: 0; right: 0; top: 160px;
    display: flex; justify-content: center; align-items: center; gap: 8px;
  }
  .icon-row__rule { width: 48px; height: 2px; background: var(--orange); margin: 0 6px; }
  .icon-tile {
    width: 28px; height: 28px; border-radius: 6px; background: var(--pink);
    display: flex; align-items: center; justify-content: center;
  }
  .contact-list {
    position: absolute; left: 0; right: 0; top: 222px; list-style: none;
    text-align: center; font-family: "Montserrat", sans-serif;
    font-size: 19px; line-height: 1.6; color: var(--muted);
  }
  .back-art {
    position: absolute; left: 30px; right: 30px; bottom: 40px; height: 330px;
    border-radius: 40px;
    background: radial-gradient(ellipse at 50% 50%, var(--art-light) 0%, var(--art-warm) 70%, var(--paper) 100%);
  }
</style>
</head>
<body>
<main class="stage">
  <section class="card card--front">
    <h1 class="brand-name">Bamboo &amp; Ember</h1>
    <p class="brand-location">Las Vegas, NV</p>
    <div class="front-art" role="img" aria-label="Cartoon curry bowl and round flatbread walking together, surrounded by pink hearts and sparkles"></div>
    <p class="tagline">“A match made in heaven”</p>
  </section>

  <section class="card card--back">
    <h2 class="holder-name">Harpreet Kalra (Toby)</h2>
    <div class="icon-row">
      <span class="icon-row__rule"></span>
      <span class="icon-tile">
        <svg width="16" height="16" viewBox="0 0 24 24" fill="#fff"><path d="M6.6 10.8a15 15 0 0 0 6.6 6.6l2.2-2.2a1 1 0 0 1 1-.25 11.4 11.4 0 0 0 3.6.57 1 1 0 0 1 1 1V20a1 1 0 0 1-1 1A17 17 0 0 1 3 4a1 1 0 0 1 1-1h3.5a1 1 0 0 1 1 1c0 1.25.2 2.45.57 3.57a1 1 0 0 1-.25 1z"/></svg>
      </span>
      <span class="icon-tile">
        <svg width="16" height="16" viewBox="0 0 24 24" fill="#fff"><path d="M3 5h18v14H3z"/><path d="M3 5l9 7 9-7" stroke="#e36b93" stroke-width="2" fill="none"/></svg>
      </span>
      <span class="icon-tile">
        <svg width="16" height="16" viewBox="0 0 24 24" fill="none" stroke="#fff" stroke-width="2"><circle cx="12" cy="12" r="9"/><path d="M3 12h18M12 3c3 3 3 15 0 18M12 3c-3 3-3 15 0 18"/></svg>
      </span>
      <span class="icon-row__rule"></span>
    </div>
    <ul class="contact-list">
      <li>(480) 555-0147</li>
      <li>TobyKalra@mailbox-demo.com</li>
      <li>www.BambooEmberLV.com</li>
    </ul>
    <div class="back-art" role="img" aria-label="Cartoon curry bowl and round flatbread walking together with pink hearts and sparkles"></div>
  </section>
</main>
</body>
</html>
```